EPC Marketing Flyer Pinefold HC

Company Name: Pinefold Homecheck Ltd
Product: Residential EPCs
Territory: Nationwide (UK)
Marketing channel: Flyer will be used for email and postal mailshots. We have not targeted this particular segment of the market before, so we need it to be eye catching, clearly messaged and encourage the recipient to get in touch.

We need a flyer to promote our services to conduct EPCs owned by public and private sector for residential ONLY (NOT Commercial), on a large or small scale.

Our Surveyors: experienced and accredited surveyors, quality service, quick and professional

Our Business: Warm Ledger Accredited, Reputation in business for excellence, fast growing

Our Service: Friendly, high quality, quick and professional

Colours: Designs in green and white (same shade as corporate colours), with our logo, and warm ledger accreditation logo, promoting our business.

Target Market(s)

Estate Agencies, Housing Associations, Local Authorities (Housing Departments), House Builders (NOT Home Owners Directly)

Industry/Entity Type

It Company

Font styles to use
Sans Serif
Other font styles liked:
• Calibri

Colors
add136
9bcb3c
cadf82
f6faec
eaf2ce

Requirements
Must have
• Our contact number etc must be clearly visible, and that we do EPCs
• Must state: What is an EPC? An EPC (Energy Performance Certificate) gives a property an energy efficiency rating from A (most efficient) to G (least efficient) and is valid for 10 years. An EPC can also provide recommendations on home improvement measures which once complete can improve the energy efficiency of the property.
• Who needs and EPC? All landlords and home owners, as all properties available to buy or rent require a valid and current EPC.
• Contact details:
• Tel: 08000 915 462
• Website: www.pinefold-hc.co.uk
• Email: epc@pinefold-hc.co.uk
• we must also be ably to print out the flyer
Nice to have
• Nice images to accompany the text which give a feeling of Environmentally Green, Home Energy Efficiency, Home Warmth and family - see example attached. And image of survey professional at work.
Should not have
• Any reference to cost or pricing
• Warm ledger logo art work must not be any other size that that specified in guidance document attached.

```html
<!DOCTYPE html>
<html lang="en">
<head>
<meta charset="utf-8">
<title>EPC Flyer – Pinefold Homecheck Ltd</title>
<link rel="stylesheet" href="https://fonts.googleapis.com/css2?family=Open+Sans:wght@400;600;700&family=Bitter:wght@700&display=swap">
<style>
  :root {
    --green-dark: #4f9a2c;
    --green: #6db33f;
    --green-bright: #9bcb3c;
    --green-soft: #cadf82;
    --green-pale: #eaf2ce;
    --green-mist: #f6faec;
    --ink: #111111;
    --paper: #ffffff;
    --frame: #222222;
    --sky: #9cc8ec;
    --sky-light: #d9ecf8;
    --grass: #5c9e2e;
  }
  html, body {
    margin: 0;
    padding: 0;
    width: 1200px;
    height: 551px;
    overflow: hidden;
    background: var(--paper);
  }
  .canvas {
    position: relative;
    width: 1200px;
    height: 551px;
    background: var(--paper);
  }
  .flyer {
    position: absolute;
    left: 38px;
    top: 32px;
    width: 679px;
    height: 483px;
    border: 1px solid var(--frame);
    background: var(--paper);
    overflow: hidden;
    font-family: "Open Sans", Calibri, sans-serif;
  }
  .flyer-art {
    position: absolute;
    left: 0;
    top: 0;
    width: 679px;
    height: 483px;
  }
  .brand {
    position: absolute;
    left: 262px;
    top: 60px;
    display: flex;
    align-items: center;
    gap: 14px;
  }
  .brand-dot {
    width: 46px;
    height: 46px;
    border-radius: 50%;
    background: var(--green);
  }
  .brand-name {
    font-family: "Open Sans", Calibri, sans-serif;
    font-weight: 600;
    font-size: 30px;
    color: var(--green);
    line-height: 1;
    letter-spacing: -0.5px;
  }
  .info-block {
    position: absolute;
    color: var(--paper);
    text-align: center;
  }
  .info-block h2 {
    margin: 0;
    font-size: 16.5px;
    font-weight: 700;
    line-height: 1.2;
  }
  .info-block p {
    margin: 0;
    font-size: 8.6px;
    line-height: 1.33;
  }
  .info-what {
    left: 0;
    top: 211px;
    width: 340px;
  }
  .info-who {
    left: 0;
    top: 310px;
    width: 380px;
  }
  .contact {
    position: absolute;
    left: 62px;
    top: 394px;
    margin: 0;
    padding: 0;
    list-style: none;
    font-family: "Bitter", Georgia, serif;
    font-weight: 700;
    font-size: 18.5px;
    line-height: 25px;
    color: var(--ink);
  }
</style>
</head>
<body>
<div class="canvas">
  <div class="flyer">
    <svg class="flyer-art" viewBox="38 32 679 483" xmlns="http://www.w3.org/2000/svg">
      <defs>
        <linearGradient id="photo-tones" x1="0" y1="0" x2="0" y2="1">
          <stop offset="0" stop-color="var(--sky)"/>
          <stop offset="0.45" stop-color="var(--sky-light)"/>
          <stop offset="0.7" stop-color="var(--green-bright)"/>
          <stop offset="1" stop-color="var(--grass)"/>
        </linearGradient>
      </defs>

      <!-- family photo area -->
      <polygon class="photo-area" role="img"
        aria-label="Smiling family of four lying together on green grass beneath a bright blue sky"
        points="40,218 165,138 300,225 405,225 432,185 718,185 718,378 430,378 400,400 40,400"
        fill="url(#photo-tones)"/>

      <!-- house silhouette -->
      <polygon class="house-shape" role="img" aria-label="Simple light green house illustration"
        points="98,178 165,128 235,178 235,400 98,400"
        fill="var(--green-bright)" opacity="0.85"/>

      <!-- roofline bands -->
      <polyline class="roofline" points="40,205 165,122 305,212 398,212 425,172 718,172"
        fill="none" stroke="var(--green)" stroke-width="5"/>
      <polyline class="roofline-thin" points="40,213 165,131 302,219 402,219 429,179 718,179"
        fill="none" stroke="var(--green-bright)" stroke-width="2"/>

      <!-- base bands -->
      <polyline class="baseline" points="40,408 404,408 432,386 718,386"
        fill="none" stroke="var(--green)" stroke-width="5"/>
      <polyline class="baseline-thin" points="40,416 408,416 436,394 718,394"
        fill="none" stroke="var(--green-bright)" stroke-width="2"/>

      <!-- text panels -->
      <path class="panel-what" d="M40,237 H332 a46,46 0 0 1 0,92 H40 Z"
        fill="var(--green)" opacity="0.88"/>
      <path class="panel-who" d="M40,337 H398 a31,31 0 0 1 0,62 H40 Z"
        fill="var(--green)" opacity="0.88"/>

      <!-- accreditation badge -->
      <rect class="accreditation-badge" x="612" y="398" width="84" height="96" rx="4"
        fill="none" stroke="var(--green)" stroke-width="3"/>
    </svg>

    <div class="brand">
      <span class="brand-dot"></span>
      <span class="brand-name">Pinefold Homecheck Ltd</span>
    </div>

    <div class="info-block info-what">
      <h2>What is an EPC?</h2>
      <p>An EPC (Energy Performance Certificate)<br>
      gives a property an energy efficiency rating from A (most efficient)<br>
      to G (least efficient) and is valid for 10 years. An EPC can also provide<br>
      recommendations on home improvement measures which once<br>
      complete can improve the energy efficiency of the property.</p>
    </div>

    <div class="info-block info-who">
      <h2>Who needs and EPC?</h2>
      <p>All landlords and home owners, as all properties available<br>
      to buy or rent require a valid and current EPC.</p>
    </div>

    <ul class="contact">
      <li>Tel: 08000 915 462</li>
      <li>Website: www.pinefold-hc.co.uk</li>
      <li>Email: epc@pinefold-hc.co.uk</li>
    </ul>
  </div>
</div>
</body>
</html>
```